Book Cover for a short book on cryptocurrency investment

I need a cover design for a book titled "Seven Quiet Rules of Ledger Wealth" with the subtitle "The Measured Pathway". The book will be freely distributed as well as available on Brindlecart. I am open to any design concept that peaks my interest. My only suggestion would be to make the design colorful, bright, and attractive but this is not set in stone. I would also like to avoid pictures of coins or crypto logos if possible.

```html
<!DOCTYPE html>
<html lang="en">
<head>
<meta charset="utf-8">
<title>Seven Quiet Rules of Ledger Wealth — Book Cover</title>
<link href="https://fonts.googleapis.com/css2?family=Raleway:wght@300;700;800&family=Encode+Sans+Semi+Condensed:wght@500&display=swap" rel="stylesheet">
<style>
  :root {
    --stage: #f1f1f1;
    --pink: #f474e8;
    --amber: #f5a84e;
    --violet: #b03de4;
    --indigo: #6a3fe8;
    --cyan: #4fd0f5;
    --white: #ffffff;
  }
  * { margin: 0; padding: 0; box-sizing: border-box; }
  html, body {
    width: 1200px;
    height: 1026px;
    overflow: hidden;
    background: var(--stage);
  }
  .canvas {
    position: relative;
    width: 1200px;
    height: 1026px;
  }
  .cover {
    position: absolute;
    left: 280px;
    top: 63px;
    width: 640px;
    height: 900px;
    overflow: hidden;
  }
  .cover-art {
    position: absolute;
    inset: 0;
    background:
      radial-gradient(ellipse 60% 40% at 15% 35%, rgba(245, 168, 78, 0.75), rgba(245, 168, 78, 0) 70%),
      radial-gradient(ellipse 55% 45% at 95% 70%, rgba(79, 208, 245, 0.8), rgba(79, 208, 245, 0) 70%),
      linear-gradient(165deg, var(--pink) 0%, var(--violet) 50%, var(--indigo) 100%);
  }
  .title-frame {
    position: absolute;
    left: 134px;
    top: 126px;
    width: 430px;
    height: 570px;
    border: 7px solid var(--white);
  }
  .title-block {
    position: absolute;
    left: 134px;
    top: 286px;
    width: 430px;
    text-align: center;
    color: var(--white);
  }
  .title-lead {
    display: block;
    font-family: "Raleway", sans-serif;
    font-weight: 300;
    font-size: 26px;
    letter-spacing: 0.5px;
    text-transform: uppercase;
  }
  .title-main {
    display: block;
    font-family: "Raleway", sans-serif;
    font-weight: 800;
    font-size: 72px;
    letter-spacing: 9px;
    line-height: 1.05;
    margin-top: 6px;
    text-transform: uppercase;
  }
  .title-second {
    display: block;
    font-family: "Raleway", sans-serif;
    font-weight: 700;
    font-size: 48px;
    letter-spacing: 1px;
    line-height: 1.1;
    text-transform: uppercase;
  }
  .subtitle {
    position: absolute;
    left: 134px;
    top: 718px;
    width: 430px;
    text-align: center;
    font-family: "Encode Sans Semi Condensed", sans-serif;
    font-weight: 500;
    font-size: 30px;
    color: var(--white);
  }
</style>
</head>
<body>
  <main class="canvas">
    <section class="cover" aria-label="Book cover">
      <div class="cover-art" role="img" aria-label="Abstract flowing colour shapes in pink, amber, violet and cyan"></div>
      <div class="title-frame"></div>
      <h1 class="title-block">
        <span class="title-lead">Seven Quiet Rules of</span>
        <span class="title-main">Ledger</span>
        <span class="title-second">Wealth</span>
      </h1>
      <p class="subtitle">The Measured Pathway</p>
    </section>
  </main>
</body>
</html>
```